International Food Manufacturer in the need of a new business card and logo.

Our Company - Brightfield Provisions Ltd.

Our Industry - Food and Drink

We are a Wild Harvested Food Distributor / Manufacturer. We service the following food sectors: Supermarkets, Hotels, Restaurants, Cafes, Catering and all people looking to eat healthy food products.

Slogan - The foremost source for everything healthy

Business card details -

48-52 Quarrow Lane
Ashby Meadow
London
NP7 3RD United Kingdom
Morven Tillick
+44 7700 900412 - UK
+971 50 5550137 - UAE
+38 067 555 0198 - Ukraine
morven@brightfieldprovisions.com
www.brightfieldprovisions.com

Goal - We are looking for a dynamic modern new look for our corporate image and a designer who can bring this new concept to our future food product designs. Please try to incorporate 3d hexagonal vector Imaging in your design concepts.

Target Market(s)

Industry/Entity Type

Food Service

Contact Information for Business Card

Brightfield Provisions Ltd.
48-52 Quarrow Lane
Ashby Meadow
London
NP7 3RD United Kingdom
Morven Tillick
+44 7700 900412 - UK
+971 50 5550137 - UAE

Font styles to use
Serif

Colors

Designer to choose colors to be used in the design.

Requirements
Must have
• Please read project description above.
Nice to have
Should not have

```html
<!DOCTYPE html>
<html lang="en">
<head>
<meta charset="utf-8">
<title>Brightfield Provisions Ltd. – Business Card</title>
<link rel="stylesheet" href="https://fonts.googleapis.com/css2?family=Montserrat:wght@500;600;700&display=swap">
<style>
  :root {
    --backdrop: #e6e8ea;
    --card: #ffffff;
    --green-dark: #5b7a3a;
    --green-light: #7aab3f;
    --ink: #1f1f1f;
    --hex-tone: #d9d9d9;
  }
  * { margin: 0; padding: 0; box-sizing: border-box; }
  html, body { width: 1200px; height: 675px; overflow: hidden; }
  body {
    background: var(--backdrop);
    font-family: "Montserrat", sans-serif;
    display: flex; align-items: center; justify-content: center;
  }
  .card {
    position: relative;
    width: 980px; height: 560px;
    background: var(--card);
    overflow: hidden;
    box-shadow: 0 6px 24px rgba(0,0,0,0.12);
  }
  .card-shapes { position: absolute; inset: 0; }
  .hex-pattern {
    position: absolute; top: 0; right: 0;
    width: 320px; height: 170px;
    background: radial-gradient(ellipse at 70% 20%, var(--hex-tone) 0%, rgba(217,217,217,0.35) 55%, rgba(255,255,255,0) 80%);
  }
  .brand {
    position: absolute; left: 120px; top: 150px;
    display: flex; align-items: center; gap: 22px;
    color: var(--green-dark); font-weight: 700;
  }
  .brand-dot {
    width: 96px; height: 96px; border-radius: 50%;
    background: var(--green-light);
  }
  .brand-name { font-size: 54px; line-height: 1; letter-spacing: -0.5px; }
  .brand-sub { font-size: 30px; line-height: 1.2; margin-top: 6px; }
  .holder-name {
    position: absolute; left: 62px; top: 470px;
    font-size: 40px; font-weight: 600; color: #fff;
  }
  .contact {
    position: absolute; left: 560px; top: 110px;
    color: var(--ink); font-size: 20px; font-weight: 500; line-height: 1.35;
  }
  .contact-row { display: flex; gap: 14px; margin-bottom: 16px; }
  .contact-row svg { flex: none; width: 24px; height: 24px; margin-top: 2px; fill: var(--green-dark); }
  .contact-row.tight { margin-bottom: 4px; }
</style>
</head>
<body>
  <div class="card">
    <svg class="card-shapes" viewBox="0 0 980 560" aria-hidden="true">
      <path d="M0,440 L300,440 C340,440 345,360 400,360 L470,360 C505,360 515,385 530,410 L590,560 L0,560 Z" fill="var(--green-dark)"/>
      <path d="M560,480 L980,460 L980,490 L575,515 Z" fill="var(--green-light)"/>
      <path d="M880,465 L920,463 L900,485 L860,488 Z" fill="var(--green-dark)"/>
      <path d="M935,462 L980,460 L980,480 L915,484 Z" fill="var(--green-dark)"/>
    </svg>

    <div class="hex-pattern" role="img" aria-label="Faint 3D hexagon pattern decoration"></div>

    <div class="brand">
      <div class="brand-dot"></div>
      <div>
        <div class="brand-name">Brightfield</div>
        <div class="brand-sub">Provisions Ltd.</div>
      </div>
    </div>

    <div class="holder-name">Morven Tillick</div>

    <div class="contact">
      <div class="contact-row">
        <svg viewBox="0 0 24 24"><path d="M12 2a7 7 0 0 0-7 7c0 5 7 13 7 13s7-8 7-13a7 7 0 0 0-7-7zm0 9.5A2.5 2.5 0 1 1 12 6.5a2.5 2.5 0 0 1 0 5z"/></svg>
        <address style="font-style:normal">48-52 Quarrow Lane<br>Ashby Meadow<br>London<br>NP7 3RD<br>United Kingdom</address>
      </div>
      <div class="contact-row">
        <svg viewBox="0 0 24 24"><path d="M6.6 10.8a15 15 0 0 0 6.6 6.6l2.2-2.2a1 1 0 0 1 1-.25 11.4 11.4 0 0 0 3.6.57 1 1 0 0 1 1 1V20a1 1 0 0 1-1 1A17 17 0 0 1 3 4a1 1 0 0 1 1-1h3.5a1 1 0 0 1 1 1c0 1.25.2 2.45.57 3.57a1 1 0 0 1-.25 1z"/></svg>
        <div>+44 7700 900412 - UK<br>+971 50 5550137 - UAE<br>+38 067 555 0198 - Ukraine</div>
      </div>
      <div class="contact-row tight">
        <svg viewBox="0 0 24 24"><path d="M3 5h18v14H3z M3 5l9 7 9-7" fill="none" stroke="var(--green-dark)" stroke-width="1.8"/></svg>
        <div>morven@brightfieldprovisions.com</div>
      </div>
      <div class="contact-row">
        <svg viewBox="0 0 24 24"><circle cx="12" cy="12" r="10"/><path d="M2 12h20M12 2c3 3 3 17 0 20M12 2c-3 3-3 17 0 20" fill="none" stroke="#fff" stroke-width="1.2"/></svg>
        <div>www.brightfieldprovisions.com</div>
      </div>
    </div>
  </div>
</body>
</html>
```